New Design required for Disposable Gloves Pack

We need a new design for our range of disposable Gloves.
The brand name is "Pardo" I will attach the existing logo.

The needs to be 3 variations of the design (maybe different colours) that we can use for the different kinds of gloves: Latex Gloves, Clear Vinyl Gloves & Blue Vinyl Gloves.
Pack size is: 220x65x120mm.

Attached is a template to use showing all sides of the pack as flat. It is preferable that you supply an image of the complete folded pack as well with your design. Also attached is a PDF of our old pack design. Please use all the text on this old design for the new one.

The packs need to be easily differentiated from each other.

Target Market(s)

New Zealand Businesses, food processors & manufacturers. Medical & health care professionals

Font styles to use
Sans Serif

Requirements
Must have
• 3 variations of the same pack design to differentiate between the 3 types of gloves we offer: Latex Gloves, Clear Vinyl & Blue Vinyl Gloves.

```html
<!DOCTYPE html>
<html lang="en">
<head>
<meta charset="utf-8">
<title>Pardo Disposable Gloves – Pack Fronts</title>
<link rel="stylesheet" href="https://fonts.googleapis.com/css2?family=Montserrat:wght@400;500;700;800&display=swap">
<style>
  :root {
    --bg: #ffffff;
    --ink: #ffffff;
    --latex-a: #12c27e;
    --latex-b: #06a869;
    --blue-a: #2445c8;
    --blue-b: #1330a8;
    --clear-a: #6a4cd0;
    --clear-b: #4b34b4;
    --brand-dark: #111111;
  }
  * { box-sizing: border-box; margin: 0; padding: 0; }
  html, body { width: 1200px; height: 1000px; overflow: hidden; background: var(--bg); }
  body { font-family: "Montserrat", sans-serif; color: var(--ink); position: relative; }

  .pack-front {
    position: absolute;
    width: 560px;
    height: 306px;
    box-shadow: 0 18px 30px rgba(0,0,0,0.18);
    overflow: hidden;
  }
  .pack-front--blue  { left: 50px;  top: 90px;  background: linear-gradient(135deg, var(--blue-a), var(--blue-b)); }
  .pack-front--clear { left: 600px; top: 290px; background: linear-gradient(135deg, var(--clear-a), var(--clear-b)); }
  .pack-front--latex { left: 250px; top: 560px; background: linear-gradient(135deg, var(--latex-a), var(--latex-b)); }

  .pack-mark {
    position: absolute; left: 26px; top: 26px;
    font-size: 40px; font-weight: 500; letter-spacing: 2px;
  }
  .dispense-window {
    position: absolute; left: 145px; top: 118px;
    width: 310px; height: 80px;
    border: 1.5px solid rgba(255,255,255,0.85);
    border-radius: 22px;
  }
  .brand-lockup {
    position: absolute; left: 30px; top: 190px;
    display: flex; align-items: center; gap: 8px;
    font-size: 26px; font-weight: 500; letter-spacing: 3px;
  }
  .brand-lockup .dot { width: 12px; height: 12px; border-radius: 50%; background: var(--ink); }
  .product-name {
    position: absolute; left: 30px; top: 228px;
    font-size: 34px; font-weight: 800; line-height: 1;
  }
  .product-type {
    position: absolute; left: 31px; top: 266px;
    font-size: 18px; font-weight: 500; letter-spacing: 1px;
  }
  .info-rule {
    position: absolute; left: 432px; top: 212px;
    width: 1px; height: 80px; background: rgba(255,255,255,0.8);
  }
  .size-label {
    position: absolute; left: 462px; top: 160px;
    font-size: 34px; font-weight: 800;
  }
  .glove-icon {
    position: absolute; left: 494px; top: 150px;
    width: 52px; height: 52px; border-radius: 8px;
    background: rgba(255,255,255,0.85);
  }
  .features {
    position: absolute; right: 18px; top: 222px;
    list-style: none; text-align: right;
    font-size: 13px; font-weight: 400; line-height: 22px;
  }

  .brand-corner {
    position: absolute; left: 880px; top: 870px;
    display: flex; align-items: center; gap: 10px;
    color: var(--brand-dark);
    font-size: 40px; font-weight: 500; letter-spacing: 4px;
  }
  .brand-corner .dot { width: 16px; height: 16px; border-radius: 50%; background: var(--brand-dark); }
</style>
</head>
<body>

  <section class="pack-front pack-front--blue" aria-label="Blue Vinyl Gloves pack front">
    <div class="pack-mark">Pardo</div>
    <div class="dispense-window"></div>
    <div class="brand-lockup"><span class="dot"></span>Pardo</div>
    <div class="product-name">BLUE VINYL</div>
    <div class="product-type">GLOVES</div>
    <div class="info-rule"></div>
    <div class="size-label">L</div>
    <div class="glove-icon" role="img" aria-label="Pair of gloves icon"></div>
    <ul class="features"><li>Ambidexterous •</li><li>Single use •</li><li>Lightly powered •</li></ul>
  </section>

  <section class="pack-front pack-front--clear" aria-label="Clear Vinyl Gloves pack front">
    <div class="pack-mark">Pardo</div>
    <div class="dispense-window"></div>
    <div class="brand-lockup"><span class="dot"></span>Pardo</div>
    <div class="product-name">CLEAR VINYL</div>
    <div class="product-type">GLOVES</div>
    <div class="info-rule"></div>
    <div class="size-label">L</div>
    <div class="glove-icon" role="img" aria-label="Pair of gloves icon"></div>
    <ul class="features"><li>Ambidexterous •</li><li>Single use •</li><li>Lightly powered •</li></ul>
  </section>

  <section class="pack-front pack-front--latex" aria-label="Latex Gloves pack front">
    <div class="pack-mark">Pardo</div>
    <div class="dispense-window"></div>
    <div class="brand-lockup"><span class="dot"></span>Pardo</div>
    <div class="product-name">LATEX</div>
    <div class="product-type">GLOVES</div>
    <div class="info-rule"></div>
    <div class="size-label">L</div>
    <div class="glove-icon" role="img" aria-label="Pair of gloves icon"></div>
    <ul class="features"><li>Ambidexterous •</li><li>Single use •</li><li>Lightly powered •</li></ul>
  </section>

  <div class="brand-corner"><span class="dot"></span>Pardo</div>

</body>
</html>
```